Pinecrest Rapids Outfitters
In the Spirit of Fun and Adventure
Pinecrest Rapids Outfitters - Travel
Creative Brief
Bright & Fun-filled
Dale Hartwin
38217 Sorrel Ln Ridgefold Crossing, MT. 59412
www.paddlevortex.example
info@paddlevortex.example
38217 Sorrel Ln
Our logo is fairly clean and simple but would like to add a fun whitewater element to the card to liven it up.
Add A : Join the Adventure on: Friendspace Logo Journey Scout logo Clip Stream Logo Chirpline Logo

```html
<!DOCTYPE html>
<html lang="en">
<head>
<meta charset="utf-8">
<title>Pinecrest Rapids Outfitters – Business Card</title>
<link rel="stylesheet" href="https://fonts.googleapis.com/css2?family=Open+Sans:wght@400;600;700&display=swap">
<style>
  :root {
    --navy: #1d2a6b;
    --navy-deep: #141d52;
    --ink: #2b2b3a;
    --card: #ffffff;
    --card-shade: #e6e8ee;
    --backdrop: #d9d4cc;
    --accent: #3b5fae;
  }
  * { box-sizing: border-box; margin: 0; padding: 0; }
  html, body { width: 1200px; height: 482px; overflow: hidden; }
  body {
    background: var(--backdrop);
    font-family: "Open Sans", Arial, sans-serif;
    color: var(--ink);
    position: relative;
  }
  .card {
    position: absolute;
    top: 92px;
    width: 545px;
    height: 362px;
    border-radius: 26px;
    background: linear-gradient(160deg, var(--card) 55%, var(--card-shade) 100%);
    box-shadow: 0 4px 14px rgba(0,0,0,0.25);
    overflow: hidden;
  }
  .card-front { left: 43px; }
  .card-back { left: 619px; }

  .side-band {
    position: absolute;
    left: 0; top: 0; bottom: 0;
    width: 55px;
    background: linear-gradient(180deg, var(--navy) 0%, var(--navy-deep) 100%);
  }

  .brand { position: absolute; display: flex; align-items: center; gap: 14px; }
  .brand-dot {
    width: 60px; height: 60px; border-radius: 50%;
    background: var(--accent);
    flex: none;
  }
  .brand-name {
    color: var(--navy);
    font-weight: 700;
    font-size: 21px;
    line-height: 1.08;
    letter-spacing: 1px;
    text-transform: uppercase;
    white-space: nowrap;
  }
  .card-front .brand { left: 28px; top: 40px; }
  .card-back .brand { left: 50%; top: 62px; transform: translateX(-50%); }

  .contact-list {
    position: absolute;
    left: 98px; top: 150px;
    list-style: none;
    font-size: 12px;
    line-height: 14.5px;
    color: var(--ink);
  }
  .contact-list li { display: flex; align-items: flex-start; gap: 14px; margin-bottom: 4px; white-space: nowrap; }
  .contact-list li.gap { margin-bottom: 13px; }
  .contact-list svg { width: 13px; height: 13px; flex: none; margin-top: 1px; fill: var(--navy); }

  .faint-mark {
    position: absolute;
    left: 398px; top: 150px;
    width: 115px; height: 115px;
    border-radius: 50%;
    background: var(--accent);
    opacity: 0.08;
  }
  .person-name {
    position: absolute;
    left: 412px; top: 205px;
    color: var(--navy);
    font-weight: 700;
    font-size: 19px;
    white-space: nowrap;
  }

  .join-title {
    position: absolute;
    top: 208px; left: 0; right: 0;
    text-align: center;
    color: var(--navy);
    font-weight: 700;
    font-size: 16px;
  }
  .social-grid {
    position: absolute;
    left: 60px; top: 262px;
    display: grid;
    grid-template-columns: 216px 230px;
    row-gap: 24px;
    list-style: none;
    font-size: 12px;
  }
  .social-grid li { display: flex; align-items: center; gap: 10px; white-space: nowrap; }
  .social-chip { width: 22px; height: 22px; border-radius: 3px; background: var(--navy); flex: none; }
</style>
</head>
<body>

<section class="card card-front">
  <div class="side-band"></div>
  <div class="brand">
    <span class="brand-dot"></span>
    <span class="brand-name">Pinecrest<br>Rapids<br>Outfitters</span>
  </div>

  <ul class="contact-list">
    <li class="gap">
      <svg viewBox="0 0 16 16"><path d="M8 1 1 7.5h2V15h4v-4h2v4h4V7.5h2z"/></svg>
      <span>38217 Sorrel Ln<br>Ridgefold Crossing, MT. 59412</span>
    </li>
    <li>
      <svg viewBox="0 0 16 16"><path d="M3.5 1.5 6 1l1.5 3.5L5.8 6a9 9 0 0 0 4.2 4.2l1.5-1.7L15 10l-.5 2.5C14 14 12 15 10 14A14 14 0 0 1 2 6C1 4 2 2 3.5 1.5z"/></svg>
      <span>(T) 8005550172</span>
    </li>
    <li>
      <svg viewBox="0 0 16 16"><path d="M3.5 1.5 6 1l1.5 3.5L5.8 6a9 9 0 0 0 4.2 4.2l1.5-1.7L15 10l-.5 2.5C14 14 12 15 10 14A14 14 0 0 1 2 6C1 4 2 2 3.5 1.5z"/></svg>
      <span>4065550318</span>
    </li>
    <li class="gap">
      <svg viewBox="0 0 16 16"><path d="M4 1h8v14H4zM5.5 2.5v9h5v-9zM7 13h2v1H7z"/></svg>
      <span>4065550847</span>
    </li>
    <li>
      <svg viewBox="0 0 16 16"><path d="M8 1a7 7 0 1 0 3.5 13l-.6-1.2A5.7 5.7 0 1 1 13.7 8v.8c0 .9-.6 1.4-1.2 1.4s-1.2-.5-1.2-1.4V5h-1.3v.6A3 3 0 1 0 10.6 10a2.4 2.4 0 0 0 4.4-1.2V8A7 7 0 0 0 8 1zm0 9a2 2 0 1 1 0-4 2 2 0 0 1 0 4z"/></svg>
      <span>info@paddlevortex.example</span>
    </li>
    <li>
      <svg viewBox="0 0 16 16"><path d="M8 1a7 7 0 1 0 0 14A7 7 0 0 0 8 1zm5.6 6.3h-2.4a11 11 0 0 0-1-4.3 5.7 5.7 0 0 1 3.4 4.3zM8 2.4c.7.9 1.5 2.6 1.7 4.9H6.3C6.5 5 7.3 3.3 8 2.4zM5.8 3a11 11 0 0 0-1 4.3H2.4A5.7 5.7 0 0 1 5.8 3zM2.4 8.7h2.4a11 11 0 0 0 1 4.3 5.7 5.7 0 0 1-3.4-4.3zM8 13.6c-.7-.9-1.5-2.6-1.7-4.9h3.4c-.2 2.3-1 4-1.7 4.9zm2.2-.6a11 11 0 0 0 1-4.3h2.4a5.7 5.7 0 0 1-3.4 4.3z"/></svg>
      <span>www.paddlevortex.example</span>
    </li>
  </ul>

  <div class="faint-mark"></div>
  <p class="person-name">Dale Hartwin</p>
</section>

<section class="card card-back">
  <div class="brand">
    <span class="brand-dot"></span>
    <span class="brand-name">Pinecrest<br>Rapids<br>Outfitters</span>
  </div>

  <p class="join-title">Join the Adventure on :</p>

  <ul class="social-grid">
    <li><span class="social-chip"></span>Friendspace@paddlevortex</li>
    <li><span class="social-chip"></span>Clip Stream@paddlevortex</li>
    <li><span class="social-chip"></span>Chirpline@paddlevortex</li>
    <li><span class="social-chip"></span>Journey Scout@paddlevortex</li>
  </ul>
</section>

</body>
</html>
```